BHSC Business cards

We are an established dental practice that is looking for new business cards to match our new logo. We are looking for something unique and sophisticated.
BRIEF: Colours are black, silver and white. Include the company name, logo (including “Pelwick Heath Dental Care”) and phone number “03 9415 2876”.
Front - Include the company name, logo (including “Pelwick Heath Dental Care”) and phone number “03 9415 2876”.
Back - Include the company name,  “Pelwick Heath Dental Care”, phone number “03 9415 2876”. address "64A Tindle Street, Pelwick Heath, Vic 3187", "Email reception@pelwickheathdentalcare.com.au", the Dentist Name " Dr ................................"  Your next appointment "Day, date and time(am/pm)".  3 lines for 3 appointments please, and at the bottom "IF UNABLE TO KEEP THIS APPOINTMENT 48 HOURS NOTICE IS REQUIRED."
Try and be creative and different with the design, i've added an image for inspiration

Target Market(s)
ALL in need of dental
Industry/Entity Type
Dental Clinic
Look and feel
Each slider illustrates characteristics of the customer's brand and the style your logo design should communicate.

```html
<!DOCTYPE html>
<html lang="en">
<head>
<meta charset="utf-8">
<title>Pelwick Heath Dental Care – Business Cards</title>
<link rel="stylesheet" href="https://fonts.googleapis.com/css2?family=Michroma&family=Open+Sans:ital,wght@0,400;0,600;0,700;1,700&display=swap">
<style>
  :root {
    --backdrop: #1c7880;
    --card-black: #050505;
    --card-white: #ffffff;
    --silver: #c9c9c9;
    --silver-dark: #8a8a8a;
    --ink: #111111;
    --title-grey: #555555;
    --rule-grey: #7a7a7a;
  }
  * { box-sizing: border-box; margin: 0; padding: 0; }
  html, body {
    width: 1200px; height: 800px; overflow: hidden;
    background: var(--backdrop);
  }
  .canvas {
    position: relative; width: 1200px; height: 800px;
  }
  .card {
    position: absolute; top: 245px;
    width: 540px; height: 310px;
    box-shadow: 0 12px 30px rgba(0,0,0,0.35);
    overflow: hidden;
  }

  /* ---------- Front (black) ---------- */
  .card-front { left: 40px; background: var(--card-black); }
  .front-rule {
    position: absolute; left: 30px; right: 30px; height: 2px;
    background: linear-gradient(90deg, #2a2a2a, #6a6a6a, #2a2a2a);
  }
  .front-rule.top { top: 62px; }
  .front-rule.bottom { top: 236px; }
  .front-mark {
    position: absolute; left: 34px; top: 92px;
    width: 98px; height: 98px; border-radius: 50%;
    background: radial-gradient(circle at 40% 35%, #e6e6e6, #9a9a9a 70%, #6d6d6d);
  }
  .front-name {
    position: absolute; left: 150px; top: 100px;
    font-family: "Michroma", sans-serif; font-weight: 400;
    color: var(--silver); letter-spacing: 1px; line-height: 1.25;
  }
  .front-name .line-main { display: block; font-size: 30px; }
  .front-name .line-sub { display: block; font-size: 16px; letter-spacing: 4px; }
  .front-phone {
    position: absolute; left: 150px; top: 196px;
    font-family: "Michroma", sans-serif; font-size: 15px;
    color: var(--silver-dark); letter-spacing: 3px;
  }

  /* ---------- Back (white) ---------- */
  .card-back { left: 620px; background: var(--card-white); font-family: "Open Sans", sans-serif; color: var(--ink); }
  .back-band {
    position: absolute; left: 0; right: 0; height: 4px;
    background: linear-gradient(90deg, #bdbdbd, #7a7a7a 60%, #4a4a4a);
  }
  .back-band.top { top: 36px; }
  .back-band.bottom { top: 268px; }
  .back-divider {
    position: absolute; left: 262px; top: 0; bottom: 0; width: 1px; background: var(--ink);
  }
  .practice {
    position: absolute; left: 20px; top: 70px; width: 226px;
  }
  .practice-accent {
    height: 4px; width: 190px; margin-left: 30px;
    background: linear-gradient(90deg, #d0d0d0, #5a5a5a);
  }
  .practice-name {
    margin-top: 10px;
    font-size: 24px; font-weight: 700; line-height: 1.15; color: var(--title-grey);
  }
  .practice-rule { height: 1px; background: var(--rule-grey); margin: 12px 0 8px; }
  .practice-contact {
    font-size: 9.3px; line-height: 1.5; text-align: center;
  }
  .appointments {
    position: absolute; left: 280px; top: 50px; width: 244px;
  }
  .dentist-line { font-size: 15px; font-weight: 600; display: flex; align-items: flex-end; }
  .dentist-line .fill { flex: 1; border-bottom: 2px dotted var(--ink); margin: 0 30px 4px 4px; }
  .dentist-role { font-size: 8px; margin-top: -2px; }
  .next-heading { font-size: 9.5px; font-weight: 700; font-style: italic; margin: 10px 0 8px; }
  .slot { display: flex; align-items: flex-end; font-size: 9.5px; margin-bottom: 10px; }
  .slot .dots { border-bottom: 1px dotted var(--ink); margin-bottom: 3px; }
  .slot .dots.date { flex: 1.3; }
  .slot .dots.time { flex: 1; }
  .notice {
    margin-top: 12px; font-size: 8.5px; text-align: center; line-height: 1.35; text-transform: uppercase;
  }
</style>
</head>
<body>
<main class="canvas">

  <section class="card card-front" aria-label="Business card front">
    <div class="front-rule top"></div>
    <div class="front-mark" aria-hidden="true"></div>
    <h1 class="front-name">
      <span class="line-main">PELWICK HEATH</span>
      <span class="line-sub">DENTAL CARE</span>
    </h1>
    <p class="front-phone">— 03 9415 2876</p>
    <div class="front-rule bottom"></div>
  </section>

  <section class="card card-back" aria-label="Appointment card back">
    <div class="back-band top"></div>
    <div class="back-band bottom"></div>
    <div class="back-divider"></div>

    <div class="practice">
      <div class="practice-accent"></div>
      <h2 class="practice-name">Pelwick Heath<br>Dental Care</h2>
      <div class="practice-rule"></div>
      <p class="practice-contact">64A Tindle Street, Pelwick Heath, Vic 3187<br>reception@pelwickheathdentalcare.com.au</p>
    </div>

    <div class="appointments">
      <p class="dentist-line">Dr <span class="fill"></span></p>
      <p class="dentist-role">Dentist</p>
      <p class="next-heading">Your Next Appointment</p>
      <p class="slot">Date<span class="dots date"></span>At<span class="dots time"></span>am / pm</p>
      <p class="slot">Date<span class="dots date"></span>At<span class="dots time"></span>am / pm</p>
      <p class="slot">Date<span class="dots date"></span>At<span class="dots time"></span>am / pm</p>
      <p class="notice">If unable to keep this appointment<br>48 hours notice is required.</p>
    </div>
  </section>

</main>
</body>
</html>
```